Commercial Bakery needs packing design for a Bread Bag.

Dorne's Bakery needs a design for a bread bag to be distributed to grocery stores. We make all kinds of breads and want this packaging to represent our company. We would like the packaging to be black and white with a fun/bubbly modern design. I have attached a few ideas of what I am looking for.
There are 5 different products. Packaging must be the same for each product except for corresponding product name, bar code and nutrional facts.
Product names:
Coconut Cream Bread
Cream Bread
Potato Rolls
Roll ups
Coconut & Raisin Bread

Our products are packaged in a 11” x 8” poly bag.
I will open 5 contracts with whoever’s design I select. I will then provide nutritional facts, barcodes for items once a contract is selected. Thank you!!

Target Market(s)

Grocery stores

Industry/Entity Type

Bakery

Requirements
Must have
• Black and White (off whites are ok)
Should not have
• Color

```html
<!DOCTYPE html>
<html lang="en">
<head>
<meta charset="utf-8">
<title>Dorne's Bakery – Coconut Cream Bread bag labels</title>
<link rel="stylesheet" href="https://fonts.googleapis.com/css2?family=Oswald:wght@500;600&family=Alfa+Slab+One&display=swap">
<style>
  :root {
    --ink: #111111;
    --paper: #ffffff;
    --crust-light: #efb25f;
    --crust: #d98b3c;
    --crust-dark: #b8652a;
    --crumb: #f3d27c;
    --coconut: #f6dcb0;
    --bubble: #e9b77c;
    --canvas: #ffffff;
  }
  * { box-sizing: border-box; margin: 0; padding: 0; }
  html, body { width: 1200px; height: 698px; overflow: hidden; background: var(--canvas); }
  .canvas { position: relative; width: 1200px; height: 698px; }
  .abs { position: absolute; }

  .loaf {
    border-radius: 95px 95px 0 0;
    background: radial-gradient(ellipse at 45% 30%, var(--crust-light), var(--crust) 60%, var(--crust-dark));
  }
  .slices {
    border-radius: 8px 8px 0 0;
    background: linear-gradient(90deg, var(--crust) 0%, var(--crumb) 25%, var(--crust-light) 50%, var(--crumb) 75%, var(--crust) 100%);
  }
  .label-white { background: var(--paper); }
  .label-bread {
    background: radial-gradient(ellipse at 50% 45%, var(--coconut), var(--crust-light) 45%, var(--crust) 80%, var(--crust-dark));
  }
  .bubbles {
    background: linear-gradient(180deg, rgba(233,183,124,.55), rgba(233,183,124,.25) 60%, rgba(190,205,220,.35));
    border-radius: 14px;
  }
  .band { background: var(--ink); }
  .band-rule { height: 1.5px; background: var(--paper); }

  .seal {
    border-radius: 50%;
    display: flex; align-items: center; justify-content: center;
    font-family: 'Oswald', sans-serif; font-weight: 600; font-size: 10px;
    text-align: center; line-height: 1.1; text-transform: uppercase;
  }
  .seal--light { background: var(--paper); color: var(--ink); }
  .seal--dark { background: var(--ink); color: var(--paper); }

  .flavor {
    text-align: center; transform: translateY(-50%);
    font-family: 'Oswald', sans-serif; font-weight: 500; font-size: 17px; line-height: 1; color: var(--ink);
  }
  .product {
    text-align: center; transform: translateY(-50%);
    font-family: 'Alfa Slab One', serif; font-size: 30px; line-height: 1; color: var(--ink);
  }

  .weight {
    display: flex; align-items: center; justify-content: center; gap: 9px;
    transform: translateY(-50%);
    font-family: 'Oswald', sans-serif; font-weight: 500; font-size: 11px; line-height: 1;
  }
  .weight b { font-size: 17px; font-weight: 500; }
  .weight .rule { flex: 1; height: 1px; margin: 0 6px; }
  .weight--dark { color: var(--ink); }
  .weight--dark .rule { background: var(--ink); }
  .weight--light { color: var(--paper); }
  .weight--light .rule { background: var(--paper); }
</style>
</head>
<body>
<main class="canvas">
  <svg width="0" height="0" style="position:absolute">
    <defs>
      <radialGradient id="loaf-tone" cx="50%" cy="45%" r="65%">
        <stop offset="0" stop-color="#f0b866"/>
        <stop offset=".65" stop-color="#d98b3c"/>
        <stop offset="1" stop-color="#b8652a"/>
      </radialGradient>
      <linearGradient id="crumb-tone" x1="0" y1="0" x2="0" y2="1">
        <stop offset="0" stop-color="#f3d27c"/>
        <stop offset="1" stop-color="#e9ad4f"/>
      </linearGradient>
      <radialGradient id="coconut-tone" cx="50%" cy="45%" r="65%">
        <stop offset="0" stop-color="#f6dcb0"/>
        <stop offset=".6" stop-color="#e7a85c"/>
        <stop offset="1" stop-color="#cc7c36"/>
      </radialGradient>
    </defs>
  </svg>

  <!-- Bag 1: white label with bubbles -->
  <section class="bag bag--dots">
    <div class="abs loaf" style="left:162px;top:170px;width:186px;height:170px" role="img" aria-label="Golden baked loaf visible through the bag"></div>
    <div class="abs label-white" style="left:150px;top:336px;width:205px;height:237px"></div>
    <div class="abs bubbles" style="left:154px;top:342px;width:32px;height:205px" role="img" aria-label="Bubbly dot pattern in warm tones"></div>
    <div class="abs bubbles" style="left:319px;top:342px;width:32px;height:205px" role="img" aria-label="Bubbly dot pattern in warm tones"></div>
    <div class="abs seal seal--light" style="left:219px;top:303px;width:66px;height:66px">Dorne's<br>Bakery</div>
    <p class="abs flavor" style="left:150px;width:205px;top:371px">Coconut Cream</p>
    <p class="abs product" style="left:150px;width:205px;top:394px">BREAD</p>
    <svg class="abs" style="left:198px;top:414px" width="105" height="117" viewBox="0 0 105 117" role="img" aria-label="Wheat-ear shaped window showing the loaf">
      <path d="M4 4 H101 V80 Q101 100 60 113 L52.5 116 L45 113 Q4 100 4 80 Z" fill="url(#loaf-tone)"/>
    </svg>
    <div class="abs weight weight--dark" style="left:150px;width:205px;top:548px"><span class="rule"></span><b>15oz</b><span>NET WT</span><b>425g</b><span class="rule"></span></div>
    <div class="abs band" style="left:150px;top:561px;width:205px;height:12px"></div>
  </section>

  <!-- Bag 2: black bands over coconut-topped loaf -->
  <section class="bag bag--band">
    <div class="abs loaf" style="left:483px;top:170px;width:192px;height:160px" role="img" aria-label="Golden baked loaf visible through the bag"></div>
    <div class="abs label-bread" style="left:474px;top:367px;width:209px;height:177px" role="img" aria-label="Loaf with coconut flake topping visible through the bag"></div>
    <div class="abs band" style="left:474px;top:326px;width:209px;height:41px"></div>
    <div class="abs band-rule" style="left:480px;top:348px;width:64px"></div>
    <div class="abs band-rule" style="left:613px;top:348px;width:64px"></div>
    <div class="abs seal seal--dark" style="left:545px;top:305px;width:66px;height:66px">Dorne's<br>Bakery</div>
    <p class="abs flavor" style="left:474px;width:209px;top:382px">Coconut Cream</p>
    <p class="abs product" style="left:474px;width:209px;top:406px">BREAD</p>
    <svg class="abs" style="left:527px;top:423px" width="98" height="112" viewBox="0 0 98 112">
      <path d="M3 3 H95 V76 Q95 95 56 108 L49 111 L42 108 Q3 95 3 76 Z" fill="none" stroke="#111" stroke-width="2"/>
    </svg>
    <div class="abs band" style="left:474px;top:544px;width:209px;height:31px"></div>
    <div class="abs weight weight--light" style="left:474px;width:209px;top:559px"><span class="rule"></span><b>15oz</b><span>NET WT</span><b>425g</b><span class="rule"></span></div>
  </section>

  <!-- Bag 3: sliced loaf, black and white label -->
  <section class="bag bag--clean">
    <div class="abs slices" style="left:813px;top:196px;width:204px;height:145px" role="img" aria-label="Stack of sliced bread visible through the bag"></div>
    <div class="abs label-white" style="left:811px;top:379px;width:211px;height:162px"></div>
    <div class="abs band" style="left:811px;top:339px;width:211px;height:40px"></div>
    <div class="abs band-rule" style="left:817px;top:360px;width:62px"></div>
    <div class="abs band-rule" style="left:954px;top:360px;width:62px"></div>
    <div class="abs seal seal--dark" style="left:883px;top:314px;width:64px;height:64px">Dorne's<br>Bakery</div>
    <p class="abs flavor" style="left:811px;width:211px;top:394px">Coconut Cream</p>
    <p class="abs product" style="left:811px;width:211px;top:418px">BREAD</p>
    <svg class="abs" style="left:864px;top:435px" width="103" height="103" viewBox="0 0 103 103" role="img" aria-label="Wheat-ear shaped window showing bread slices">
      <path d="M3 3 H100 V68 Q100 86 59 99 L51.5 102 L44 99 Q3 86 3 68 Z" fill="url(#crumb-tone)" stroke="#111" stroke-width="2"/>
    </svg>
    <div class="abs band" style="left:811px;top:541px;width:211px;height:34px"></div>
    <div class="abs weight weight--light" style="left:811px;width:211px;top:557px"><span class="rule"></span><b>15oz</b><span>NET WT</span><b>425g</b><span class="rule"></span></div>
  </section>
</main>
</body>
</html>
```